Private Visitenkarte für Naturwissenschaftler
Vielen Dank für die überaus gute und überzeugende Arbeit. Ohne Einschränkung weiterzuempfehlen!
Zielgruppe
Die Zielgruppe sind primär potentielle Arbeitgeber. Diese sind vor allem in der Forschung und Entwicklung im naturwissenschaftlich-technischem Bereich angesiedelt.
Aufgabenstellung
Vorraussetzungen:
1. Die Karte ist zweiseitig bedruckt
2. Auf der Vorderseite steht der Spruch:
"Wenn es schon einem gelungen ist,
so ist es keine Schwierigkeit.
Wenn es noch keinem gelungen ist,
so wird es dafür langsam Zeit!"
3. Auf der Rückseite stehen die Kontaktdaten
4. Auf beiden Seiten ist ein Hintergrund zu sehen.
Die Datei nsg.pdf beinhaltet die sogenannten Navier-Stokesschen Gleichungen. Diese beschreiben Flüssigkeitsströmungen. Der Hintergrund sollte so aufgebaut sein, dass er zum einen diese Gleichungen enthält (exakt wie dargestellt) und zum anderen etwas, dass durch die Gleichungen beschrieben wird, z.B. ein Wasserfall oder der Fluss durch ein Rohr oder auch gerne etwas Abstraktes.
Die Gestaltung also hauptsächlich den Hintergund, sowie Form, Farbe und Ausrichtung des Textes.
Da sich Rufnummern oder E-Mails immer mal ändern, benötige ich am Ende außerdem ein Dateiformat, das das Editieren der Texte erlaubt (am besten als photoshop document).
Anm.: In der Formel ist ein kleiner Fehler, in der zweiten Zeile muss das "u" ein "v" sein

```html
<!DOCTYPE html>
<html lang="de">
<head>
<meta charset="utf-8">
<title>Visitenkarte Ulrich Kivor</title>
<link rel="stylesheet" href="https://fonts.googleapis.com/css2?family=Roboto+Condensed:wght@400;500&family=Tinos&display=swap">
<style>
  :root {
    --page: #ffffff;
    --sky-deep: #34496e;
    --sky-mid: #7f96bd;
    --sky-light: #eef2f8;
    --water-teal: #5fa896;
    --water-light: #e9f2f3;
    --waterline: #1f2a38;
    --text-light: #ffffff;
    --formula: #1e3350;
  }
  * { margin: 0; padding: 0; box-sizing: border-box; }
  html, body { width: 1200px; height: 886px; overflow: hidden; background: var(--page); }
  .canvas { position: relative; width: 1200px; height: 886px; }
  .card { position: absolute; width: 604px; height: 405px; overflow: hidden; }
  .card--front { left: 0; top: 2px; }
  .card--back { left: 564px; top: 453px; }

  .card__photo { position: absolute; inset: 0; }
  .card--front .card__photo {
    background:
      linear-gradient(90deg, rgba(255,255,255,0.9) 0%, rgba(233,242,243,0.6) 45%, var(--water-teal) 100%) 0 270px / 100% 135px no-repeat,
      radial-gradient(ellipse at 75% 95%, var(--sky-light) 0%, var(--sky-mid) 45%, var(--sky-deep) 100%) 0 0 / 100% 270px no-repeat;
  }
  .card--back .card__photo {
    background:
      linear-gradient(90deg, var(--water-teal) 0%, rgba(233,242,243,0.6) 55%, rgba(255,255,255,0.9) 100%) 0 269px / 100% 136px no-repeat,
      radial-gradient(ellipse at 25% 95%, var(--sky-light) 0%, var(--sky-mid) 45%, var(--sky-deep) 100%) 0 0 / 100% 269px no-repeat;
  }
  .card__waterline { position: absolute; left: 0; right: 0; height: 2px; background: var(--waterline); opacity: 0.8; }
  .card--front .card__waterline { top: 269px; }
  .card--back .card__waterline { top: 268px; }

  .quote {
    position: absolute; right: 290px; top: 38px;
    font-family: "Roboto Condensed", sans-serif; font-weight: 500;
    font-size: 20px; line-height: 27.5px; color: var(--text-light);
    text-align: right; white-space: nowrap;
  }
  .quote__stanza + .quote__stanza { margin-top: 6px; }

  .formula {
    position: absolute; left: 364px; top: 322px;
    font-family: "Tinos", serif; font-size: 20px; color: var(--formula);
    white-space: nowrap;
  }
  .formula__line { display: flex; align-items: center; gap: 4px; }
  .formula__frac { display: inline-flex; flex-direction: column; align-items: center; line-height: 18px; }
  .formula__frac span:first-child { border-bottom: 1px solid var(--formula); }
  .formula__line--second { margin-top: 4px; padding-left: 63px; }

  .contact {
    position: absolute; left: 320px; top: 44px;
    font-family: "Roboto Condensed", sans-serif; font-weight: 500;
    color: var(--text-light); white-space: nowrap;
  }
  .contact__name, .contact__title { font-size: 20px; line-height: 28px; }
  .contact__list { list-style: none; margin-top: 16px; }
  .contact__item { display: flex; align-items: center; gap: 8px; font-size: 20px; line-height: 25.5px; }
  .contact__icon { width: 20px; height: 20px; flex: none; }
</style>
</head>
<body>
<main class="canvas">
  <section class="card card--front">
    <div class="card__photo" role="img" aria-label="Foto: Wasserstrahl, der in eine Wasseroberfläche fließt, mit Luftblasen unter Wasser"></div>
    <div class="card__waterline"></div>
    <blockquote class="quote">
      <p class="quote__stanza">„Wenn es schon einem gelungen ist,<br>so ist es keine Schwierigkeit.</p>
      <p class="quote__stanza">Wenn es noch keinem gelungen ist,<br>so wird es dafür langsam Zeit!“</p>
    </blockquote>
    <div class="formula">
      <div class="formula__line">
        <span class="formula__frac"><span>∂v</span><span><i>∂t</i></span></span>
        <span>+ (v·∇)v = <i>ν</i>△v − ∇<i>p</i> + f</span>
      </div>
      <div class="formula__line formula__line--second">∇· v = 0</div>
    </div>
  </section>

  <section class="card card--back">
    <div class="card__photo" role="img" aria-label="Foto: Wasserstrahl, der in eine Wasseroberfläche fließt, mit Luftblasen unter Wasser"></div>
    <div class="card__waterline"></div>
    <div class="contact">
      <p class="contact__name">Ulrich Kivor</p>
      <p class="contact__title">Dipl.-Math. und Dipl.-Phys.</p>
      <ul class="contact__list">
        <li class="contact__item">
          <svg class="contact__icon" viewBox="0 0 20 20" aria-hidden="true"><circle cx="10" cy="10" r="9.5" fill="#fff"/><path d="M6 5.5l2 0 1 3-1.3 1a6 6 0 0 0 2.8 2.8l1-1.3 3 1 0 2c-5 .5-9-3.5-8.5-8.5z" fill="#34496e"/></svg>
          <span>05678 246813</span>
        </li>
        <li class="contact__item">
          <svg class="contact__icon" viewBox="0 0 20 20" aria-hidden="true"><circle cx="10" cy="10" r="9.5" fill="#fff"/><rect x="6.5" y="4" width="7" height="12" rx="1.3" fill="none" stroke="#34496e" stroke-width="1.6"/></svg>
          <span>0172 9753108</span>
        </li>
        <li class="contact__item">
          <svg class="contact__icon" viewBox="0 0 20 20" aria-hidden="true"><circle cx="10" cy="10" r="9.5" fill="#fff"/><text x="10" y="14.5" text-anchor="middle" font-family="Arial, sans-serif" font-size="14" fill="#34496e">@</text></svg>
          <span>ulrich.kivor@feldnetz.de</span>
        </li>
      </ul>
    </div>
  </section>
</main>
</body>
</html>
```